Vellorine Baby Collection

We are creating the label for baby skin care products for our existing skin care brand called Vellorine. we want to play on sophistication of Vellorine current labelling and change to include kids/baby look and feel but keeping the up market style. We will have full range of different products like
1.Shampoo and Body Wash
2. Healing Cream
3. Nappy Rush Cream
4. Baby Massage Gel
5.Baby Bubble Bath
6.Baby Soothing Skin Lotion

Target Market(s)

Our target market are customers in Australia and Asia looking to purchase quality skin care products for their new born babies and young children

Industry/Entity Type

Skin care

Requirements
Must have
• some children look combined with an existing Vellorine brand
Nice to have
• maybe some baby toys and letters around the main name Vellorine

```html
<!DOCTYPE html>
<html lang="en">
<head>
<meta charset="utf-8">
<title>Vellorine Baby – Labels</title>
<link rel="stylesheet" href="https://fonts.googleapis.com/css2?family=Abril+Fatface&family=Montserrat:wght@400;600&display=swap">
<style>
  :root {
    --bg: #e4e4e6;
    --paper: #f4f4f3;
    --brand: #e0294f;
    --pink-title: #d77c93;
    --pink-band-a: #e2a2b4;
    --pink-band-b: #c45f7b;
    --blue-title: #6c9fcf;
    --blue-band-a: #9cc0e4;
    --blue-band-b: #6f9fd0;
    --band-text: #ffffff;
  }
  * { margin: 0; padding: 0; box-sizing: border-box; }
  html, body { width: 1200px; height: 1200px; overflow: hidden; }
  body {
    background: var(--bg);
    font-family: "Montserrat", sans-serif;
    display: flex;
    align-items: center;
    justify-content: center;
    gap: 60px;
  }
  .label {
    width: 480px;
    height: 640px;
    background: var(--paper);
    display: flex;
    flex-direction: column;
    box-shadow: 0 12px 30px rgba(0,0,0,0.08);
  }
  .label__top {
    flex: 1;
    display: flex;
    flex-direction: column;
    align-items: center;
    padding-top: 48px;
  }
  .brand-name {
    font-family: "Abril Fatface", serif;
    color: var(--brand);
    font-size: 40px;
    line-height: 1;
    letter-spacing: 1px;
    text-align: center;
  }
  .product-title {
    font-family: "Abril Fatface", serif;
    line-height: 0.9;
    text-align: center;
    margin-top: auto;
    margin-bottom: 30px;
  }
  .label--body .product-title { color: var(--pink-title); font-size: 120px; }
  .label--shampoo .product-title { color: var(--blue-title); font-size: 92px; margin-bottom: 70px; }
  .label__band {
    height: 250px;
    color: var(--band-text);
    padding: 26px 40px 22px;
    display: flex;
    flex-direction: column;
    align-items: center;
  }
  .label--body .label__band { background: linear-gradient(100deg, var(--pink-band-a), var(--pink-band-b)); }
  .label--shampoo .label__band { background: linear-gradient(100deg, var(--blue-band-a), var(--blue-band-b)); }
  .range-name { font-weight: 600; font-size: 28px; letter-spacing: 1.5px; }
  .range-sub { font-size: 20px; letter-spacing: 0.5px; margin-top: 2px; }
  .features {
    display: flex;
    align-items: center;
    justify-content: space-between;
    width: 100%;
    margin-top: 22px;
  }
  .feature { display: flex; align-items: center; gap: 12px; }
  .feature__icon { width: 44px; height: 44px; }
  .feature__text { font-size: 15px; line-height: 1.05; }
  .feature__text strong { display: block; font-weight: 400; font-size: 20px; }
  .origin-badge { width: 70px; height: 70px; }
  .usage { margin-top: auto; font-size: 15px; letter-spacing: 0.5px; }
</style>
</head>
<body>

<article class="label label--body">
  <div class="label__top">
    <p class="brand-name">Vellorine Baby</p>
    <h1 class="product-title">Body<br>Wash</h1>
  </div>
  <div class="label__band">
    <p class="range-name">Vellorine</p>
    <p class="range-sub">Herbal Nourishing</p>
    <div class="features">
      <div class="feature">
        <svg class="feature__icon" viewBox="0 0 44 44" aria-hidden="true">
          <circle cx="22" cy="22" r="22" fill="rgba(255,255,255,0.25)"/>
          <path d="M22 10 C27 18 30 22 30 26 A8 8 0 0 1 14 26 C14 22 17 18 22 10Z" fill="#fff"/>
        </svg>
        <p class="feature__text"><strong>7 in 1</strong>Collagen &amp;<br>essential oils</p>
      </div>
      <svg class="origin-badge" viewBox="0 0 70 70" role="img" aria-label="Origin badge">
        <circle cx="35" cy="35" r="35" fill="rgba(255,255,255,0.25)"/>
      </svg>
    </div>
    <p class="usage">FOR EVERYDAY USE · 500ml</p>
  </div>
</article>

<article class="label label--shampoo">
  <div class="label__top">
    <p class="brand-name">Vellorine Baby</p>
    <h1 class="product-title">Shampoo</h1>
  </div>
  <div class="label__band">
    <p class="range-name">Vellorine</p>
    <p class="range-sub">Herbal Nourishing</p>
    <div class="features">
      <div class="feature">
        <svg class="feature__icon" viewBox="0 0 44 44" aria-hidden="true">
          <circle cx="22" cy="22" r="22" fill="rgba(255,255,255,0.25)"/>
          <path d="M22 10 C27 18 30 22 30 26 A8 8 0 0 1 14 26 C14 22 17 18 22 10Z" fill="#fff"/>
        </svg>
        <p class="feature__text"><strong>7 in 1</strong>Collagen &amp;<br>essential oils</p>
      </div>
      <svg class="origin-badge" viewBox="0 0 70 70" role="img" aria-label="Origin badge">
        <circle cx="35" cy="35" r="35" fill="rgba(255,255,255,0.25)"/>
      </svg>
    </div>
    <p class="usage">FOR EVERYDAY USE · 500ml</p>
  </div>
</article>

</body>
</html>
```